Web site design for BrixaForm Software (www.brixaformsoftware.example)

Need the design as well as the html for the website. The brief is given in the attached file.
If possible, would like to use pencil sketches instead of images to give a unique look to the site.
Target Market(s)
small Software product companies
Industry/Entity Type
Software
Coding
Coded - Design and coding required
Number of Pages Required
5+ page

```html
<!DOCTYPE html>
<html lang="en">
<head>
<meta charset="utf-8">
<title>BrixaForm Software</title>
<link rel="stylesheet" href="https://fonts.googleapis.com/css2?family=Montserrat:wght@400;600;700;800&family=Open+Sans:wght@300;400;600&display=swap">
<style>
:root{
  --red:#d0121b;
  --black:#111;
  --ink:#1a1a1a;
  --text:#777;
  --grey-bar:#b5b5b5;
  --line:#dcdcdc;
  --footer:#232323;
  --white:#fff;
  --faint:#efefef;
}
*{margin:0;padding:0;box-sizing:border-box}
html,body{width:1200px;height:2462px;overflow:hidden;background:var(--white)}
body{position:relative;font-family:"Open Sans",Arial,sans-serif;color:var(--text)}
.abs{position:absolute}

/* header */
.site-header{left:0;top:0;width:1200px;height:67px;background:var(--white)}
.brand{left:159px;top:17px;font:700 30px/1 "Montserrat",Arial,sans-serif;letter-spacing:9px;color:var(--ink);text-transform:uppercase}
.main-nav{left:555px;top:0;height:67px;width:390px;border-left:1px solid var(--line);border-right:1px solid var(--line);display:flex;align-items:center;gap:31px;padding-left:35px}
.main-nav a{font:700 12px "Montserrat",Arial,sans-serif;color:var(--ink);text-decoration:none}
.main-nav a.active{color:var(--red)}
.header-icons{left:975px;top:22px;display:flex;gap:22px}

/* sub nav */
.sub-nav{left:0;top:67px;width:1200px;height:38px;background:var(--grey-bar)}
.sub-nav ul{list-style:none;position:absolute;left:159px;top:0;display:flex;height:38px}
.sub-nav li{font:700 11px/38px "Montserrat",Arial,sans-serif;color:var(--white);padding:0 14px}
.sub-nav li.current{background:var(--black)}
.newsletter-link{left:937px;top:8px;display:flex;align-items:center;gap:8px;font:600 11px "Montserrat",Arial,sans-serif;color:var(--white)}

/* hero */
.hero{left:0;top:105px;width:1200px;height:450px;overflow:hidden}
.hero-photo{left:0;top:0;width:1200px;height:450px;background:linear-gradient(100deg,#e9e3d8 0%,#f4efe6 55%,#d8cfbf 100%)}
.hero-red{left:0;top:0;width:1200px;height:450px;background:linear-gradient(90deg,#c4141a,#e32a2a);clip-path:polygon(0 0,854px 0,758px 450px,0 450px)}
.hero-title{right:161px;top:148px;text-align:right;font:800 60px/1.2 "Montserrat",Arial,sans-serif;color:var(--white);text-transform:uppercase;letter-spacing:-1px}

/* labels */
.section-label{height:42px;padding:0 24px;background:var(--black);color:var(--white);font:700 15px/42px "Montserrat",Arial,sans-serif;text-transform:uppercase;border-bottom:3px solid var(--red)}
.section-label.grey{background:#a7a7a7;border-bottom:none;line-height:39px}

/* about */
.watermark{left:312px;top:570px;font:800 330px/1 "Montserrat",Arial,sans-serif;color:var(--faint);letter-spacing:-8px}
.about-title{left:159px;top:695px;font:700 21px "Montserrat",Arial,sans-serif;color:var(--ink)}
.body-copy{font:300 13px/19px "Open Sans",Arial,sans-serif;color:var(--text)}
.learn-more{font:400 12px "Open Sans",Arial,sans-serif;color:var(--ink)}
.pager{display:flex;gap:8px}
.pager span{width:26px;height:26px;border-radius:50%;display:flex;align-items:center;justify-content:center;background:#eee}
.pager span.on{background:var(--black)}
.divider{left:159px;top:994px;width:1041px;height:1px;background:var(--line)}

/* services */
.service{width:200px}
.service-icon{width:50px;height:50px}
.service h3{margin-top:24px;font:700 13px "Montserrat",Arial,sans-serif;color:var(--ink)}
.service p{margin-top:8px;font:300 13px/19px "Open Sans",Arial,sans-serif;color:var(--text)}
.btn{display:inline-block;width:69px;height:31px;font:700 11px/31px "Montserrat",Arial,sans-serif;color:var(--white);text-align:center;text-transform:uppercase;background:var(--black)}
.btn.red{background:var(--red)}
.service .btn{margin-top:12px}

/* work with us */
.work-band{left:0;top:1384px;width:1200px;height:447px;background:linear-gradient(100deg,#1c2029 0%,#2a3340 40%,#1a2230 75%,#0f141c 100%)}
.work-title{left:159px;top:1531px;width:560px;font:700 21px/27px "Montserrat",Arial,sans-serif;color:var(--white);text-transform:uppercase}
.work-copy{left:159px;top:1610px;width:540px;font:400 13px/20px "Open Sans",Arial,sans-serif;color:#e3e3e3}

/* case studies */
.case-title{left:159px;top:1978px;width:460px;font:700 21px/27px "Montserrat",Arial,sans-serif;color:var(--ink);text-transform:uppercase}
.case-copy{left:159px;top:2042px;width:540px}
.case-photo{left:698px;top:1905px;width:502px;height:303px;background:linear-gradient(120deg,#d9cfc0,#f3ede4 55%,#c9b9a3);clip-path:polygon(65px 0,502px 0,502px 303px,0 303px)}

/* newsletter */
.dash{left:0;top:2266px;width:1200px;border-top:1px dashed #cfcfcf}
.subscribe-title{left:243px;top:2304px;font:700 16px "Montserrat",Arial,sans-serif;color:var(--ink)}
.email-field{left:479px;top:2295px;width:366px;height:40px;border:1px solid #e3e3e3;padding-left:16px;font:400 12px/38px "Open Sans",Arial,sans-serif;color:#999}
.signup{left:862px;top:2297px;width:103px;height:36px;background:var(--red);color:var(--white);font:700 13px/36px "Montserrat",Arial,sans-serif;text-align:center}

/* footer */
.footer-bar{left:0;top:2367px;width:1200px;height:54px;background:var(--footer)}
.footer-links{left:159px;top:2386px;font:400 11px "Open Sans",Arial,sans-serif;color:#bbb;word-spacing:2px}
.social{left:913px;top:2381px;display:flex;gap:7px}
.social span{width:26px;height:26px;border:1.5px solid #ddd;border-radius:50%}
.copyright{left:159px;top:2439px;font:400 11px "Open Sans",Arial,sans-serif;color:#444}
.legal{right:161px;top:2439px;font:400 11px "Open Sans",Arial,sans-serif;color:#444}
</style>
</head>
<body>

<header class="site-header abs">
  <div class="brand abs">BrixaForm</div>
  <nav class="main-nav abs">
    <a class="active" href="#">HOME</a><a href="#">ABOUT US</a><a href="#">SERVICES</a><a href="#">CONTACT US</a>
  </nav>
  <div class="header-icons abs">
    <svg width="18" height="18" viewBox="0 0 18 18" fill="none" stroke="#111" stroke-width="2"><circle cx="7.5" cy="7.5" r="5.5"/><path d="M11.5 11.5l5 5"/></svg>
    <svg width="18" height="20" viewBox="0 0 18 20" fill="none" stroke="#111" stroke-width="1.6"><circle cx="9" cy="6" r="4.5"/><path d="M1.5 19c0-5 3.5-7 7.5-7s7.5 2 7.5 7z"/></svg>
  </div>
</header>

<nav class="sub-nav abs">
  <ul>
    <li class="current">EXPERTISE</li><li>ENGAGEMENT MODELS</li><li>AGILE</li><li>CASE STUDIES</li><li>WORK WITH US</li><li>ACCOLADES</li><li>PARTNERS</li>
  </ul>
  <div class="newsletter-link abs">
    <svg width="22" height="22" viewBox="0 0 22 22" fill="none" stroke="#fff" stroke-width="1.5"><circle cx="11" cy="11" r="10"/><rect x="6" y="7.5" width="10" height="7"/><path d="M6 7.5l5 4 5-4"/></svg>
    NEWSLETTER
  </div>
</nav>

<section class="hero abs">
  <div class="hero-photo abs" role="img" aria-label="Hand touching a tablet showing a software engineering cycle: planning, testing, programming, development, implementation"></div>
  <div class="hero-red abs"></div>
  <h1 class="hero-title abs">Welcome to<br>BrixaForm</h1>
</section>

<section class="about">
  <div class="watermark abs">Brixa</div>
  <div class="section-label abs" style="left:159px;top:625px">About Us</div>
  <h2 class="about-title abs">BrixaForm</h2>
  <p class="body-copy abs" style="left:159px;top:734px;width:860px">We are seasoned programmers, interested in the science as well as the craft of programming.</p>
  <p class="body-copy abs" style="left:159px;top:773px;width:860px">We need to put high res black and white photos of Aravind – followed by a paragraph about Aravind<br>Ditto with Keshav and Dinesh are primarily server side programmers with expertise in large scale projects – be it Software development tools,<br>Distributed software frameworks, Telecom and mediation software or Business intelligence.</p>
  <span class="learn-more abs" style="left:159px;top:849px">Learn more</span>
  <div class="pager abs" style="left:161px;top:903px">
    <span class="on"><svg width="8" height="8" viewBox="0 0 8 8"><path d="M6 0L1 4l5 4z" fill="#fff"/></svg></span>
    <span><svg width="8" height="8" viewBox="0 0 8 8"><path d="M2 0l5 4-5 4z" fill="#111"/></svg></span>
  </div>
  <div class="divider abs"></div>
</section>

<section class="services">
  <div class="section-label abs" style="left:159px;top:1059px">Our Services</div>
  <div class="service abs" style="left:161px;top:1133px">
    <svg class="service-icon" viewBox="0 0 50 50" fill="none"><circle cx="25" cy="25" r="23.5" stroke="#d0121b" stroke-width="2.5"/><rect x="16" y="14" width="17" height="21" stroke="#555" stroke-width="2"/><path d="M19 20h11M19 24h11M19 28h7" stroke="#555" stroke-width="1.6"/></svg>
    <h3>POC</h3>
    <p>Whether it is a mobile or web<br>app prototype,</p>
    <span class="btn red">More</span>
  </div>
  <div class="service abs" style="left:386px;top:1133px">
    <svg class="service-icon" viewBox="0 0 50 50" fill="none" stroke="#777" stroke-width="2"><circle cx="25" cy="25" r="23.5"/><path d="M25 13l10 5v12l-10 5-10-5V18z M15 18l10 5 10-5 M25 23v12"/></svg>
    <h3>Build Products</h3>
    <p>Our team of analysts, design<br>thinkers and technologists...</p>
    <span class="btn">More</span>
  </div>
  <div class="service abs" style="left:621px;top:1133px">
    <svg class="service-icon" viewBox="0 0 50 50" fill="none" stroke="#777" stroke-width="2"><circle cx="25" cy="25" r="23.5"/><path d="M15 15l20 20M35 15L15 35M14 33l3 3M33 14l3 3"/></svg>
    <h3>Maintain Products</h3>
    <p>We have the ability to quickly<br>understand large,</p>
    <span class="btn">More</span>
  </div>
  <div class="service abs" style="left:854px;top:1133px">
    <svg class="service-icon" viewBox="0 0 50 50" fill="none" stroke="#777" stroke-width="2"><circle cx="25" cy="25" r="23.5"/><path d="M17 12h12l5 5v21H17z"/><rect x="15" y="23" width="21" height="9" fill="#fff"/><text x="25.5" y="30.5" font-family="Montserrat,sans-serif" font-size="7" font-weight="700" fill="#777" stroke="none" text-anchor="middle">ODC</text></svg>
    <h3>ODC Setup</h3>
    <p>We help in setting up Offshore<br>Development centres for...</p>
    <span class="btn">More</span>
  </div>
</section>

<section class="work">
  <div class="work-band abs" role="img" aria-label="Dark blurred city skyline with streams of binary digits"></div>
  <div class="section-label grey abs" style="left:159px;top:1465px">Work With Us</div>
  <h2 class="work-title abs">Work with usAutomation for VARs – New Product Development</h2>
  <p class="work-copy abs">BrixaForm works with startups and midsize product development companies. It uses design thinking and rigorouse software development principles to build world class products.</p>
  <span class="btn red abs" style="left:159px;top:1719px">More</span>
</section>

<section class="cases">
  <div class="section-label abs" style="left:159px;top:1906px">Case Studies</div>
  <h2 class="case-title abs">Automation for VARs – New Product Development</h2>
  <p class="body-copy case-copy abs">StackVend is a complete automation system for VARS – it has an ecommerce storefront, customizable catalog, Rich content crawler, Sales Quoting, Integration with Distributor systems, Asset Tracking etc.<br>Developed in VentelJS and NodraKit</p>
  <span class="learn-more abs" style="left:159px;top:2143px">Learn More</span>
  <div class="pager abs" style="left:161px;top:2184px">
    <span class="on"><svg width="8" height="8" viewBox="0 0 8 8"><path d="M6 0L1 4l5 4z" fill="#fff"/></svg></span>
    <span><svg width="8" height="8" viewBox="0 0 8 8"><path d="M2 0l5 4-5 4z" fill="#111"/></svg></span>
  </div>
  <div class="case-photo abs" role="img" aria-label="Hand holding a tablet with a software engineering cycle diagram above it"></div>
</section>

<section class="subscribe">
  <div class="dash abs"></div>
  <div class="subscribe-title abs">Subscribe our Newsletter</div>
  <div class="email-field abs">Enter your email id</div>
  <div class="signup abs">SIGN UP</div>
</section>

<footer>
  <div class="footer-bar abs"></div>
  <div class="footer-links abs">Home&nbsp; / &nbsp;Service&nbsp; / &nbsp;About Us&nbsp; / &nbsp;Expertise&nbsp; / &nbsp;Case Studies&nbsp; / &nbsp;Work With us&nbsp; / &nbsp;Contact Us</div>
  <div class="social abs"><span></span><span></span><span></span><span></span></div>
  <div class="copyright abs">© Copyright 2017 BrixaForm. All Rights Reserved</div>
  <div class="legal abs">Privacy Policy &nbsp;/ &nbsp;Terms of Service</div>
</footer>

</body>
</html>
```